New Business Card Design Project

I need a clean, professional business card. I'd like it to have some color, but not be wild. We do technology consulting and we have clients large and small who trust us with some of their most important data and projects. Simple but not boring should drive all design proposals. Multicolored and two sided, but with a matte finish, I think.
For more on tone, check out our website: http://quorvantis.example

Target Market(s)

Upper management of respected businesses. Tech savvy, but not "hipster".

Industry/Entity Type

Business

Requirements
Must have
• Files need to be provided in .eps and in .pdf in a manner that allows for easy updates.
Must have Name, Title, Phone, Email, Twitter, Website
Nice to have
• Logo/Name shouldn't be too big. One thing I've read several places is that the bigger the logo, the smaller the brand. A good article on dos and don'ts here: http://www.brindlepost.example/2011/02/business-card-experience.html

```html
<!DOCTYPE html>
<html lang="en">
<head>
<meta charset="utf-8">
<title>Quorvantis Business Card</title>
<link rel="stylesheet" href="https://fonts.googleapis.com/css2?family=Source+Sans+3:wght@400;600&display=swap">
<style>
  :root {
    --teal: #3bb8a8;
    --teal-deep: #15463f;
    --teal-mid: #1f6b62;
    --lime: #7fef06;
    --ink: #666666;
    --ice: #dcfdfd;
    --paper: #ffffff;
  }
  html, body {
    margin: 0;
    padding: 0;
    width: 1015px;
    height: 1200px;
    overflow: hidden;
    background: var(--paper);
    font-family: "Source Sans 3", "Myriad Pro", sans-serif;
  }
  .canvas { position: relative; width: 1015px; height: 1200px; }

  /* Front side */
  .card-front {
    position: absolute; left: 38px; top: 49px;
    width: 938px; height: 534px;
    border: 1px solid #222; box-sizing: border-box;
    background: var(--paper); overflow: hidden;
  }
  .holder { position: absolute; left: 0; right: 0; top: 258px; text-align: center; }
  .holder-name { margin: 0; font-size: 47px; font-weight: 400; color: var(--teal); line-height: 1; }
  .holder-title { margin: 8px 0 0; font-size: 23px; color: var(--ink); line-height: 1; }

  .contact-row {
    position: absolute; left: 24px;
    display: flex; align-items: center; gap: 8px;
    font-size: 20px; line-height: 1; color: var(--ink);
  }
  .contact-row svg { flex: none; }
  .row-social { top: 418px; }
  .row-phone { top: 456px; }
  .row-email { top: 495px; color: #ffffff; }

  .rule-thin {
    position: absolute; left: 0; right: 0; top: 443px; height: 6px;
    background: linear-gradient(90deg, var(--lime) 0%, var(--lime) 70%, var(--teal) 100%);
  }
  .band-contact {
    position: absolute; left: 0; right: 0; top: 483px; height: 40px;
    background: linear-gradient(90deg, var(--lime) 0%, var(--lime) 60%, #42c98a 100%);
  }
  .brand-box {
    position: absolute; right: 2px; top: 449px; width: 264px; height: 34px;
    border: 3px solid var(--teal); border-bottom: none; border-left: none;
    box-sizing: border-box;
    display: flex; align-items: center; justify-content: flex-end; gap: 10px;
    padding-right: 20px;
  }
  .brand-mark { width: 14px; height: 14px; border-radius: 50%; background: var(--teal); }
  .brand-name { font-size: 28px; font-weight: 400; color: var(--ink); letter-spacing: 1px; line-height: 1; }
  .site {
    position: absolute; right: 26px; top: 494px;
    font-size: 20px; color: #ffffff; line-height: 1;
  }

  /* Back side */
  .card-back {
    position: absolute; left: 41px; top: 616px;
    width: 939px; height: 537px; overflow: hidden;
  }
  .back-texture {
    position: absolute; inset: 0;
    background: linear-gradient(90deg, #3ab6ac 0%, var(--teal-mid) 22%, var(--teal-deep) 58%, var(--teal-deep) 100%);
  }
  .back-band {
    position: absolute; left: 2px; right: 0; top: 230px; height: 66px;
    background: var(--ice);
  }
  .back-pill {
    position: absolute; left: 2px; top: 240px; width: 253px; height: 46px;
    background: var(--lime); border-radius: 0 23px 23px 0;
  }
  .back-brand {
    position: absolute; left: 262px; top: 230px; height: 66px;
    display: flex; align-items: center; gap: 40px;
  }
  .back-brand .brand-mark { width: 22px; height: 22px; }
  .back-brand .brand-name { font-size: 62px; letter-spacing: 2px; }
</style>
</head>
<body>
<div class="canvas">

  <section class="card-front" aria-label="Business card front">
    <div class="holder">
      <h1 class="holder-name">Dana Whitfield</h1>
      <p class="holder-title">Managing Director</p>
    </div>

    <div class="contact-row row-social">
      <svg width="34" height="28" viewBox="0 0 34 28" aria-hidden="true"><circle cx="17" cy="14" r="12" fill="var(--teal)"/></svg>
      <span>@QUORVANTIS</span>
    </div>

    <div class="rule-thin"></div>

    <div class="contact-row row-phone">
      <svg width="38" height="26" viewBox="0 0 38 26" aria-hidden="true">
        <path d="M3 9 Q19 -1 35 9 L33 13 L27 11 L27 7 Q19 4 11 7 L11 11 L5 13 Z" fill="var(--teal)"/>
        <path d="M10 12 L28 12 L32 24 L6 24 Z" fill="none" stroke="var(--teal)" stroke-width="2.4"/>
        <circle cx="19" cy="18" r="3.5" fill="none" stroke="var(--teal)" stroke-width="2"/>
      </svg>
      <span>+1 (800) 555-0147</span>
    </div>

    <div class="brand-box">
      <span class="brand-mark"></span>
      <span class="brand-name">Quorvantis</span>
    </div>

    <div class="band-contact"></div>

    <div class="contact-row row-email">
      <svg width="34" height="24" viewBox="0 0 34 24" aria-hidden="true">
        <rect x="2" y="2" width="30" height="20" rx="2" fill="none" stroke="#ffffff" stroke-width="3"/>
        <path d="M4 5 L17 15 L30 5" fill="none" stroke="#ffffff" stroke-width="3"/>
      </svg>
      <span>web_inquiry@quorvantis.example</span>
    </div>

    <span class="site">www.quorvantis.example</span>
  </section>

  <section class="card-back" aria-label="Business card back">
    <div class="back-texture" role="img" aria-label="Crinkled paper texture in deep teal tones"></div>
    <div class="back-band"></div>
    <div class="back-pill"></div>
    <div class="back-brand">
      <span class="brand-mark"></span>
      <span class="brand-name">Quorvantis</span>
    </div>
  </section>

</div>
</body>
</html>
```